eBook and paperback cover

I need an eBook cover (planned release via Vandrel and Quorm) and subsequently also a paperback cover (planned release via Luteph), which looks appealing even in black and white and small format and reflects the following novel content.

The text consists of about 420 standard pages - how many pages the paperback will have in the end, I cannot say at the moment. Thus the cover should be designed in a way that the thickness of the spine can be adjusted by me if necessary. Please also take necessary crop margins into account with regard to the paperback cover.

Book title: Das Erbe, das im Nebel schläft
Author: Marlene Quastorf
Untertitel: Roman

General information about the content:

The core theme of the story is jealousy and self-identity: Emma, the main character (= 18 years old, long brown hair, brown eyes, pretty), finds out that her sister Céline (= 18 years old, dark-blond hair, brown-green eyes, thin) that is at the same age, lives the life of her dreams. Later she finds out, that her sisters life is not the way she imagined in the beginning – nothing is, what it seems to be.

Other relevant characters are Ferdinand (father of Emma and Céline), his friend and business partner Karl) and Emmas mother, the maid (Ekaterina).

The novel takes place in Vienna (Austria).

Blurb:

When Emma surprisingly finds out that she is adopted and is supposed to be the daughter of the wealthy Austrian Ferdinand and his maid Ekaterina, she scents a chance to escape her miserable life. Full of hope she travels to Vienna, where she experiences a bitter disappointment: Her father is anything but happy to see her, Ekaterina in not there and her half-sister Céline, who is the same age, seems to be living the life of her dreams.

But it was to get even worse: Back at home, Emma gradually slipped away from everything she had clung to in life. In her desperation, she is angry at her father, whom she blames for her fate, and jealous of her half-sister. In her quest for retribution, Emma becomes entangled in a maelstrom of intrigue that is set to change her life forever and put her understanding of justice to the test.

Target Market(s)

Women (age 28-65)

Colors
d3a5cc
b8a6cd
eea4c8
f59195
fabb94
fbc994
85acd3
fbf289

Requirements
Must have
• ebook cover (vandrel standard size) and paperback cover (DIN A5)
Nice to have
• Colors as selected below (but please not all of them)

```html
<!DOCTYPE html>
<html lang="de">
<head>
<meta charset="utf-8">
<title>Das Erbe, das im Nebel schläft – Marlene Quastorf</title>
<link rel="stylesheet" href="https://fonts.googleapis.com/css2?family=Oswald:wght@500;600&display=swap">
<style>
  :root {
    --sky-light: #eeeeee;
    --sky-mid: #d6d6d6;
    --field-dark: #7a7a7a;
    --title-peach: rgba(236, 160, 124, 0.86);
    --title-outline: rgba(90, 50, 35, 0.7);
    --band-lavender: rgba(139, 130, 190, 0.85);
    --author-white: #ffffff;
  }
  html, body {
    margin: 0;
    padding: 0;
    width: 800px;
    height: 1200px;
    overflow: hidden;
    background: #ffffff;
  }
  .cover {
    position: relative;
    width: 800px;
    height: 1200px;
    overflow: hidden;
    font-family: "Oswald", "Arial Narrow", sans-serif;
  }
  .cover-photo {
    position: absolute;
    inset: 0;
    width: 100%;
    height: 100%;
  }
  .title {
    position: absolute;
    top: 40px;
    left: 0;
    width: 100%;
    margin: 0;
    text-align: center;
    font-weight: 500;
    font-size: 228px;
    line-height: 198px;
    letter-spacing: -4px;
    color: var(--title-peach);
    -webkit-text-stroke: 1px var(--title-outline);
  }
  .title-line {
    display: block;
  }
  .author-band {
    position: absolute;
    left: 0;
    top: 1083px;
    width: 100%;
    height: 54px;
    background: var(--band-lavender);
    display: flex;
    align-items: center;
    justify-content: center;
  }
  .author-name {
    margin: 0;
    font-weight: 600;
    font-size: 31px;
    letter-spacing: 0.32em;
    color: var(--author-white);
    padding-left: 0.32em;
  }
</style>
</head>
<body>
  <main class="cover">
    <svg class="cover-photo" viewBox="0 0 800 1200" preserveAspectRatio="none" role="img" aria-label="Black-and-white photograph of two young blond women seen from behind, holding hands in a grassy meadow under a pale sky">
      <defs>
        <linearGradient id="meadow-sky" x1="0" y1="0" x2="0" y2="1">
          <stop offset="0" stop-color="#e4e4e4"/>
          <stop offset="0.5" stop-color="#eeeeee"/>
          <stop offset="0.78" stop-color="#cfcfcf"/>
          <stop offset="1" stop-color="#8a8a8a"/>
        </linearGradient>
      </defs>
      <rect width="800" height="1200" fill="url(#meadow-sky)"/>
    </svg>

    <h1 class="title">
      <span class="title-line">Das</span>
      <span class="title-line">Erbe,</span>
      <span class="title-line">das im</span>
      <span class="title-line">Nebel</span>
      <span class="title-line">schläft</span>
    </h1>

    <div class="author-band">
      <p class="author-name">Marlene Quastorf</p>
    </div>
  </main>
</body>
</html>
```